Driving-coach/trainer who wants to inform about the offer and how I can help people to drive more re

I need a flyer that informs potential customers about my offer.

DL size 210 mm x 99 mm, vertical!

I'm a trainer/coach who helps people to drive a car more relaxed, without fear and more confident.

It's a one to one training. I do train people in their own car. It gets people their freedom back to go where and when they like to go by own car...

Target Market(s)

People (man an woman) who are afraid of driving a car, or are very stressed while driving....

Industry/Entity Type

Life Coaching

Font styles to use
Sans Serif

Colors
acd136

Requirements
Must have
• Page 1:
• -my offer (see text-pdf)
• -three fotos (see attached files "Pixmarra") of people who are satisfied with my offer
• Page 2:
• -advantages in the work with me.
• -contact information
• -and a picture of me (see attached file) next to the contact information or the advantages of my work
• -my logo (see attached file) on Page 1 + 2
• -i like a "clear" and structured layout. "Less is more"

```html
<!DOCTYPE html>
<html lang="de">
<head>
<meta charset="utf-8">
<title>Fahrangst-Bewältigungs-Coach – Flyer</title>
<link rel="stylesheet" href="https://fonts.googleapis.com/css2?family=Roboto+Condensed:wght@400;700&family=Arimo:wght@400;700&family=Nunito:wght@400;600&display=swap">
<style>
  :root {
    --lime: #a8cf38;
    --lime-dark: #8fb82a;
    --grey-top: #9e9da2;
    --grey-bottom: #b9b8bc;
    --ink: #111111;
    --white: #ffffff;
    --stage: #e9e9e6;
  }
  * { box-sizing: border-box; margin: 0; padding: 0; }
  html, body { width: 1200px; height: 1200px; overflow: hidden; background: var(--stage); }
  .canvas { position: relative; width: 1200px; height: 1200px; }
  .flyer { position: absolute; top: 146px; width: 462px; height: 907px; overflow: hidden; box-shadow: 0 2px 10px rgba(0,0,0,.18); }
  .flyer--front { left: 85px; background: var(--lime); }
  .flyer--back { left: 660px; background: var(--white); }

  /* front */
  .hero { position: absolute; left: 0; top: 0; width: 462px; height: 598px;
    background: linear-gradient(180deg, var(--grey-top), var(--grey-bottom)); }
  .hero__intro { position: absolute; left: 57px; top: 50px; font: 400 38px/1 "Arimo", sans-serif; color: var(--ink); }
  .hero__question { position: absolute; left: 57px; font: 700 37px/1.08 "Roboto Condensed", sans-serif; color: var(--white); }
  .hero__question--1 { top: 112px; }
  .hero__question--2 { top: 176px; }
  .hero__question--3 { top: 272px; }
  .coach-photo { position: absolute; left: 290px; top: 314px; width: 172px; height: 284px;
    background: radial-gradient(ellipse at 45% 28%, #b08a73 0 18%, transparent 19%),
                linear-gradient(180deg, transparent 0 40%, #f4f4f2 41%);
  }
  .callout { position: absolute; left: 0; top: 379px; width: 281px; height: 184px; background: var(--lime); padding: 16px 0 0 56px; }
  .callout__lead { font: 700 25px/1.2 "Arimo", sans-serif; color: var(--ink); }
  .callout__ask { margin-top: 6px; font: 700 24px/1.25 "Arimo", sans-serif; color: var(--white); }
  .brand { position: absolute; left: 0; top: 598px; width: 462px; height: 68px; background: var(--white); padding: 6px 0 0 57px; }
  .brand__name { font: 400 27px/1.1 "Nunito", sans-serif; letter-spacing: 2.2px; color: var(--lime-dark); }
  .brand__role { font: 400 18px/1.2 "Nunito", sans-serif; letter-spacing: 1.9px; color: var(--lime-dark); margin-top: 2px; }
  .situations { position: absolute; left: 57px; top: 680px; width: 385px; list-style: none; }

  .checklist li { position: relative; padding-left: 20px; font: 400 12.6px/1.27 "Roboto Condensed", sans-serif; color: var(--ink); margin-bottom: 5px; }
  .checklist li svg { position: absolute; left: 0; top: 3px; width: 11px; height: 11px; }

  /* back */
  .steps { position: absolute; left: 0; top: 0; width: 462px; height: 201px; background: var(--lime); padding: 52px 20px 0 56px; }
  .steps__title { font: 700 23px/1.1 "Roboto Condensed", sans-serif; color: var(--white); }
  .steps__sub { font: 400 19px/1.2 "Arimo", sans-serif; color: var(--white); margin: 2px 0 8px; }
  .benefits { position: absolute; left: 0; top: 201px; width: 462px; height: 237px; padding: 8px 20px 0 56px; }
  .benefits__title { font: 700 23px/1.1 "Roboto Condensed", sans-serif; color: var(--lime); margin-bottom: 8px; }
  .benefits .checklist li { margin-bottom: 4px; }
  .photo { position: absolute; }
  .photo--convertible { left: 0; top: 438px; width: 227px; height: 116px; background: linear-gradient(135deg, #6f7a7c, #c9a57a 60%, #e7d9c3); }
  .photo--window { left: 235px; top: 438px; width: 227px; height: 116px; background: linear-gradient(135deg, #bfc8a8, #5f6466 55%, #e6c9a6); }
  .photo--road-trip { left: 0; top: 558px; width: 462px; height: 204px; background: linear-gradient(180deg, #5f93cf 0%, #a9c7e6 32%, #4d6b34 45%, #a88f55 65%, #c2a76a 100%); }
  .contact { position: absolute; left: 0; top: 762px; width: 462px; height: 145px; background: var(--lime); text-align: center; padding-top: 6px; }
  .contact__name { font: 400 17px/1.2 "Arimo", sans-serif; color: var(--ink); }
  .contact__role { font: 400 9px/1.2 "Arimo", sans-serif; color: var(--ink); }
  .contact__phone { font: 700 25px/1.1 "Arimo", sans-serif; color: var(--white); margin-top: 10px; }
  .contact__web { font: 700 15.5px/1.2 "Arimo", sans-serif; color: var(--white); }
</style>
</head>
<body>
<svg width="0" height="0" style="position:absolute" aria-hidden="true">
  <symbol id="tick-box" viewBox="0 0 12 12">
    <rect x="0.7" y="1.7" width="9" height="9" fill="none" stroke="#111" stroke-width="1.2"/>
    <path d="M2.6 6.2 L5 8.6 L11.3 0.8" fill="none" stroke="#111" stroke-width="1.5"/>
  </symbol>
</svg>

<main class="canvas">
  <section class="flyer flyer--front">
    <div class="hero">
      <p class="hero__intro">Wollen Sie endlich...</p>
      <h1 class="hero__question hero__question--1">Fahrangst überwinden?</h1>
      <h2 class="hero__question hero__question--2">Panikattacken beim<br>Autofahren loswerden?</h2>
      <h2 class="hero__question hero__question--3">Oder einfach sicher<br>Autofahren?</h2>
      <div class="coach-photo" role="img" aria-label="Portrait der Trainerin in weißer Bluse"></div>
      <div class="callout">
        <p class="callout__lead">Dann sind Sie<br>hier richtig!</p>
        <p class="callout__ask">Kommt Ihnen eine<br>dieser Situationen<br>bekannt vor?</p>
      </div>
    </div>
    <div class="brand">
      <p class="brand__name">Sabine Kalterborn</p>
      <p class="brand__role">Fahrangst-Bewältigungs-Coach</p>
    </div>
    <ul class="situations checklist">
      <li><svg><use href="#tick-box"/></svg>Angst oder Panikattacken begleiten Sie beim Autofahren. Vielleicht vermeiden Sie deshalb das Autofahren komplett. - Sie möchten angstfrei und/oder ohne Panikattacken fahren.</li>
      <li><svg><use href="#tick-box"/></svg>Sie trauen sich das Autofahren nicht (mehr) zu. - Sie wünschen sich, sicher, entspannt und stressfrei Auto zu fahren.</li>
      <li><svg><use href="#tick-box"/></svg>Autofahren erleben Sie unter hoher Anspannung und Stress. - Sie wünschen sich, Autofahren sicher und entspannt zu erleben.</li>
      <li><svg><use href="#tick-box"/></svg>Bestimmte Situationen (z.B. Autobahn, Baustellen, Stadtverkehr...) bereiten Ihnen großen Stress. - Sie möchten diese Situationen souveräner meistern.</li>
    </ul>
  </section>

  <section class="flyer flyer--back">
    <div class="steps">
      <h2 class="steps__title">Das muss nicht so bleiben!</h2>
      <p class="steps__sub">3 Schritte zur Lösung</p>
      <ul class="checklist">
        <li><svg><use href="#tick-box"/></svg>Erstgespräch vereinbaren</li>
        <li><svg><use href="#tick-box"/></svg>Analyse Ihrer individuellen Situation und Zielsetzung</li>
        <li><svg><use href="#tick-box"/></svg>Individuelles Coaching und Training (ggf. Fahrangst-Therapie - als psychotherapeutische Heilpraktikerin bin ich auf Angst- und Panikstörungen spezialisiert)</li>
      </ul>
    </div>
    <div class="benefits">
      <h2 class="benefits__title">Advantages in the work with me</h2>
      <ul class="checklist">
        <li><svg><use href="#tick-box"/></svg>über 10 Jahre Erfahrung als Trainerin und Coach im Bereich Fahrsicherheit.</li>
        <li><svg><use href="#tick-box"/></svg>Als psychotherapeutische Heilpraktikerin<br>bin ich auf Angststörungen und Panikattacken spezialisiert</li>
        <li><svg><use href="#tick-box"/></svg>100 % auf Sie zugeschnitten: ich hole Sie genau dort ab, wo Sie jetzt stehen und unterstütze Sie in Ihrem Prozess individuell und zielführend.</li>
        <li><svg><use href="#tick-box"/></svg>Wenn es Ihnen nicht möglich ist, in meine Praxis nach Lindenfeld Nord zu kommen: Mit der mobilen Praxis komme ich auch zu Ihnen.</li>
        <li><svg><use href="#tick-box"/></svg>Termine sind auch abends und am Wochenende möglich.</li>
      </ul>
    </div>
    <div class="photo photo--convertible" role="img" aria-label="Zufriedene Fahrerin im Cabrio"></div>
    <div class="photo photo--window" role="img" aria-label="Lächelnde Fahrerin am Autofenster mit Daumen hoch"></div>
    <div class="photo photo--road-trip" role="img" aria-label="Gelber Kleinwagen mit Koffern auf dem Dach in einer Sommerwiese"></div>
    <div class="contact">
      <p class="contact__name">Sabine Kalterborn</p>
      <p class="contact__role">Fahrangst-Bewältigungs-Coach</p>
      <p class="contact__phone">Tel. 0152 41 87 36 09</p>
      <p class="contact__web">www.ruhig-am-steuer.de</p>
    </div>
  </section>
</main>
</body>
</html>
```